Classy business card for accounting firm

We're looking for a new business card for our accounting firm. Our logo was designed by Brandolith, so all of the design info we would like to use has been provided. The specific font provided isn't required to be used.

We want the card to look classy and elegent. Probably more minimalistic, but still with some pops of color.

The options we would like to include on the card are as follows:
1. Main office phone line
2. Direct phone line
3. Email address
4. Website URL
5. Name
6. Title (CEO, President, etc.)
7. Firm Address

The design and card should be double sided!!! The drop down box in the project brief for some reason is defaulting to single sided. Not sure why this is happening.

Thanks!

Contact Information for Business Card

The options we would like to include on the card are as follows: 1. Main office phone line 2. Direct phone line 3. Email address 4. Website URL 5. Name 6. Title (CEO, President, etc.) 7. Firm Address

Requirements
Must have
• Card must be double sided.

```html
<!DOCTYPE html>
<html lang="en">
<head>
<meta charset="utf-8">
<title>Ledgerwell Associates – Business Card</title>
<link href="https://fonts.googleapis.com/css2?family=Montserrat:wght@400;500;700&display=swap" rel="stylesheet">
<style>
  :root {
    --page-bg: #e9e9e9;
    --card-white: #f7f7f6;
    --card-grey: #6f6f6f;
    --ink: #5c5c5c;
    --ink-light: #7a7a7a;
    --orange: #ee7f2d;
    --white: #ffffff;
  }
  * { box-sizing: border-box; margin: 0; padding: 0; }
  html, body { width: 1200px; height: 853px; overflow: hidden; }
  body {
    background: var(--page-bg);
    font-family: "Montserrat", Arial, sans-serif;
    display: flex;
    align-items: center;
    justify-content: center;
    gap: 50px;
  }
  .card {
    position: relative;
    width: 530px;
    height: 303px;
    border-radius: 22px;
    overflow: hidden;
    box-shadow: 0 6px 18px rgba(0,0,0,0.12);
  }

  /* Back side */
  .card-back { background: var(--card-grey); }
  .card-back .pattern-area {
    position: absolute; inset: 0;
    background: linear-gradient(135deg, #747474 0%, #6a6a6a 55%, #7a7a7a 100%);
  }
  .back-name {
    position: absolute;
    left: 0; right: 0; top: 136px;
    display: flex; align-items: center; justify-content: center; gap: 12px;
    color: var(--white);
    font-size: 26px;
    font-weight: 500;
  }
  .back-name .name-mark {
    width: 14px; height: 14px; background: var(--white);
  }

  /* Front side */
  .card-front { background: var(--card-white); color: var(--ink); }
  .person { position: absolute; left: 32px; top: 34px; }
  .person .name {
    color: var(--orange); font-weight: 700; font-size: 20px; letter-spacing: 0.5px;
  }
  .person .title { font-size: 13px; color: var(--ink-light); margin-top: 2px; }
  .divider {
    position: absolute; left: 30px; right: 30px; top: 102px;
    height: 1px; background: #8a8a8a;
  }
  .contact-list {
    position: absolute; left: 32px; top: 114px;
    list-style: none; font-size: 12px; color: var(--ink-light); line-height: 1.55;
  }
  .contact-list li { display: flex; align-items: center; gap: 7px; }
  .contact-list svg { width: 10px; height: 10px; flex: none; }
  .front-name {
    position: absolute; right: 30px; top: 40px;
    display: flex; align-items: center; gap: 8px;
    font-size: 16px; font-weight: 500; color: var(--ink);
  }
  .front-name .name-mark {
    width: 10px; height: 10px; border-radius: 50%; background: var(--orange);
  }
  .address {
    position: absolute; right: 32px; bottom: 30px; text-align: right;
    font-size: 12px; line-height: 1.45; color: var(--ink-light);
  }
  .address .label { color: var(--orange); }
</style>
</head>
<body>

  <section class="card card-back" aria-label="Card back">
    <div class="pattern-area" role="img" aria-label="Faint repeating brand pattern in grey tones"></div>
    <div class="back-name">
      <span class="name-mark"></span>
      <span>Ledgerwell Associates</span>
    </div>
  </section>

  <section class="card card-front" aria-label="Card front">
    <div class="person">
      <div class="name">NAME</div>
      <div class="title">Title(CEO,President,etc)</div>
    </div>

    <div class="front-name">
      <span class="name-mark"></span>
      <span>Ledgerwell Associates</span>
    </div>

    <div class="divider"></div>

    <ul class="contact-list">
      <li>
        <svg viewBox="0 0 10 10"><path d="M2 1 L4 1 L4.6 3 L3.5 3.8 Q4.5 5.8 6.2 6.5 L7 5.4 L9 6 L9 8 Q5 9 2 6 Q0.8 3.5 2 1Z" fill="var(--orange)"/></svg>
        Main office phone line
      </li>
      <li>
        <svg viewBox="0 0 10 10"><rect x="2.5" y="0.5" width="5" height="9" rx="1" fill="none" stroke="var(--orange)" stroke-width="1.2"/></svg>
        Direct phone
      </li>
      <li>
        <svg viewBox="0 0 10 10"><rect x="0.5" y="2" width="9" height="6.5" fill="var(--orange)"/><path d="M0.5 2 L5 5.5 L9.5 2" fill="none" stroke="var(--card-white)" stroke-width="0.9"/></svg>
        email address
      </li>
      <li>
        <svg viewBox="0 0 10 10"><circle cx="5" cy="5" r="4.5" fill="var(--orange)"/><path d="M0.5 5 H9.5 M5 0.5 V9.5" stroke="var(--card-white)" stroke-width="0.7"/><ellipse cx="5" cy="5" rx="2" ry="4.5" fill="none" stroke="var(--card-white)" stroke-width="0.7"/></svg>
        websiteURL
      </li>
    </ul>

    <div class="address">
      <div class="label">Firm address</div>
      <div>Address Line one,</div>
      <div>City, State, Country</div>
    </div>
  </section>

</body>
</html>
```